The Bright Socket Business cards

one side I would like my logo (uploaded) and the other side I want my details. I'm an electrician in sydney. The logo side I'm happy with just a white background and our logo in the middle.

Details for other side
24/7 Sydney Electrician
Marcus Hale
0431 758 216
marcus@thebrightsocket.com.au
thebrightsocket.com.au
icons for facebook, instagram, linked in

electrician

company info

```html
<!DOCTYPE html>
<html lang="en">
<head>
<meta charset="utf-8">
<title>The Bright Socket – Business Cards</title>
<link href="https://fonts.googleapis.com/css2?family=Lexend:wght@400;600;700&display=swap" rel="stylesheet">
<style>
  :root {
    --stage: #222222;
    --brand-red: #ea3424;
    --cream: #f6e6d4;
    --ink: #111111;
    --paper: #ffffff;
  }
  * { box-sizing: border-box; margin: 0; padding: 0; }
  html, body { width: 1200px; height: 711px; overflow: hidden; }
  body {
    background: var(--stage);
    font-family: "Lexend", Arial, sans-serif;
    position: relative;
  }
  .card {
    position: absolute;
    top: 200px;
    width: 540px;
    height: 310px;
    border-radius: 22px;
    overflow: hidden;
  }
  .card--front { left: 40px; background: var(--brand-red); }
  .card--back { left: 620px; background: var(--paper); }

  .front-wordmark {
    position: absolute;
    inset: 0;
    display: flex;
    align-items: center;
    justify-content: center;
    color: var(--cream);
    font-weight: 700;
    font-size: 40px;
    letter-spacing: 1px;
  }

  .name-tab {
    position: absolute;
    top: 0; right: 0;
    width: 26px; height: 74px;
    background: var(--brand-red);
  }
  .person {
    position: absolute;
    top: 26px; right: 42px;
    text-align: right;
  }
  .person__name { color: var(--brand-red); font-weight: 700; font-size: 28px; line-height: 1; }
  .person__role { color: var(--ink); font-weight: 600; font-size: 12px; margin-top: 4px; }

  .back-wordmark {
    position: absolute;
    top: 92px; left: 28px;
    color: var(--brand-red);
    font-weight: 700;
    font-size: 30px;
  }
  .tagline {
    position: absolute;
    top: 148px; left: 30px;
    color: var(--brand-red);
    font-weight: 600;
    font-size: 13px;
    letter-spacing: 0.5px;
  }
  .contacts {
    position: absolute;
    top: 176px; left: 30px;
    list-style: none;
  }
  .contacts li {
    display: flex;
    align-items: center;
    gap: 8px;
    color: var(--ink);
    font-size: 12.5px;
    font-weight: 600;
    height: 20px;
  }
  .contacts svg { width: 13px; height: 13px; flex: none; }

  .wave { position: absolute; inset: 0; width: 540px; height: 310px; }

  .follow {
    position: absolute;
    right: 28px; bottom: 92px;
    display: flex;
    align-items: center;
    gap: 8px;
    color: var(--paper);
    font-weight: 600;
    font-size: 13px;
  }
  .follow__dot {
    width: 18px; height: 18px;
    border-radius: 50%;
    background: var(--paper);
  }
</style>
</head>
<body>

  <section class="card card--front" aria-label="Business card, logo side">
    <div class="front-wordmark">The Bright Socket</div>
  </section>

  <section class="card card--back" aria-label="Business card, details side">
    <svg class="wave" viewBox="0 0 540 310" aria-hidden="true">
      <path d="M0 310 L0 292 C190 292 300 270 370 205 C430 148 480 128 540 124 L540 310 Z" fill="var(--brand-red)"/>
      <path d="M0 284 C150 286 270 268 345 226" fill="none" stroke="var(--ink)" stroke-width="3"/>
    </svg>

    <div class="name-tab"></div>
    <div class="person">
      <div class="person__name">Marcus Hale</div>
      <div class="person__role">Electrician</div>
    </div>

    <div class="back-wordmark">The Bright Socket</div>
    <div class="tagline">24/7 SYDNEY ELECTRICIAN</div>

    <ul class="contacts">
      <li>
        <svg viewBox="0 0 24 24" aria-hidden="true"><path fill="var(--brand-red)" d="M6.6 10.8a15 15 0 0 0 6.6 6.6l2.2-2.2c.3-.3.7-.4 1-.2 1.1.4 2.3.6 3.6.6.6 0 1 .4 1 1V20c0 .6-.4 1-1 1A17 17 0 0 1 3 4c0-.6.4-1 1-1h3.5c.6 0 1 .4 1 1 0 1.3.2 2.5.6 3.6.1.3 0 .7-.2 1z"/></svg>
        0431 758 216
      </li>
      <li>
        <svg viewBox="0 0 24 24" aria-hidden="true"><g fill="none" stroke="var(--brand-red)" stroke-width="2"><circle cx="12" cy="12" r="9"/><path d="M3 12h18M12 3c3 3 3 15 0 18M12 3c-3 3-3 15 0 18"/></g></svg>
        www.thebrightsocket.com.au
      </li>
      <li>
        <svg viewBox="0 0 24 24" aria-hidden="true"><g fill="none" stroke="var(--brand-red)" stroke-width="2"><rect x="3" y="5" width="18" height="14" rx="1"/><path d="M3 6l9 7 9-7"/></g></svg>
        marcus@thebrightsocket.com.au
      </li>
    </ul>

    <div class="follow">
      <span>Follow us</span>
      <span class="follow__dot"></span>
      <span class="follow__dot"></span>
      <span class="follow__dot"></span>
    </div>
  </section>

</body>
</html>
```